Pebbleton Default Template Pages

I have a logo designed for my web and mobile based app. I would like a set of matching templates designed to present the various types of content the app will deliver to users. Please design for me a set of html and css based templates to present the web based content.
The chosen template designs will have a colour scheme complimentary to my existing Pebbleton logo. I have attached the Pebbleton Logo.

```html
<!DOCTYPE html>
<html lang="en">
<head>
<meta charset="utf-8">
<title>Pebbleton – Home</title>
<link href="https://fonts.googleapis.com/css2?family=Lato:ital,wght@0,400;0,700;0,900;1,400&display=swap" rel="stylesheet">
<style>
:root{
  --blue:#0f5fa8;
  --navy:#1a56a0;
  --red:#e3204f;
  --yellow:#f8cf3a;
  --green:#1e9e1e;
  --ink:#1c1c1c;
  --muted:#555;
  --white:#fff;
}
*{box-sizing:border-box;margin:0;padding:0}
html,body{width:1200px;height:2404px;overflow:hidden}
body{font-family:'Lato',sans-serif;color:var(--ink);background:var(--white);position:relative}
.abs{position:absolute}
.topbar{left:0;top:0;width:1200px;height:31px;background:var(--blue);color:var(--white);font-size:13px}
.topbar span{position:absolute;top:8px;display:flex;align-items:center;gap:7px}
.nav{left:0;top:31px;width:1200px;height:64px;background:var(--white);font-size:15.5px}
.nav a{position:absolute;top:22px;color:var(--ink);text-decoration:none}
.btn{background:var(--red);color:var(--white);border-radius:20px;font-weight:700;font-size:16px;display:flex;align-items:center;justify-content:center}
.logo-plate{left:516px;top:0;width:169px;height:176px}
.brand{left:516px;top:100px;width:169px;text-align:center;color:var(--navy);font-weight:700;font-size:24px}
.hero{left:0;top:95px;width:1200px;height:640px}
.hero h1{position:absolute;left:113px;top:185px;color:var(--white);font-weight:700;font-size:76px;line-height:76px;width:620px}
.phone{border-radius:26px;border:5px solid #d9d9de;background:#222}
.phone div{position:absolute;inset:4px;border-radius:20px}
.cat-title{left:0;top:800px;width:1200px;text-align:center;font-weight:700;font-size:52px}
.cat{width:294px;height:294px;border-radius:50%;top:895px;display:flex;align-items:flex-end;justify-content:center;padding-bottom:34px;color:var(--white);font-weight:700;font-size:27px}
.arrow{width:35px;height:35px;top:1015px}
.feature-img{left:115px;top:1275px;width:616px;height:436px;border-radius:4px;background:linear-gradient(120deg,#5da83a 0%,#c9a776 40%,#e8c07e 60%,#f5c93a 85%,#e8e2d4 100%)}
.feature h2{position:absolute;left:113px;top:1742px;color:var(--green);font-weight:700;font-size:26px}
.feature p{position:absolute;left:113px;width:610px;font-size:15px;line-height:25.6px;color:#222}
.readmore{left:112px;top:2172px;color:var(--green);font-style:italic;font-size:15px}
.news{left:776px;top:1273px;width:314px;height:918px;background:var(--white);box-shadow:0 0 6px rgba(0,0,0,.25);border:1px solid #ddd}
.news-head{left:795px;top:1300px;width:283px;height:47px;background:var(--red);color:var(--white);font-size:31px;font-weight:700;display:flex;align-items:center;justify-content:center}
.item{left:798px;width:270px}
.item .thumb{width:181px;height:104px}
.item h3{font-size:15.5px;font-weight:700;color:var(--navy);margin-top:14px}
.item time{display:block;font-size:11.5px;color:#555;margin-top:5px}
.item p{font-size:14.5px;line-height:20.5px;color:#444;margin-top:6px}
.item a{display:block;font-size:13.5px;color:var(--navy);font-weight:700;text-decoration:underline;margin-top:6px}
.footer{left:0;top:2277px;width:1200px;height:127px;background:var(--blue);color:var(--white);font-size:15.5px}
.footer .links{position:absolute;left:112px;top:54px}
.footer .links span.sep{margin:0 12px}
</style>
</head>
<body>

<div class="abs topbar">
  <span style="left:111px"><svg width="9" height="12" viewBox="0 0 9 12"><path d="M4.5 0A4.5 4.5 0 0 0 0 4.5C0 8 4.5 12 4.5 12S9 8 9 4.5A4.5 4.5 0 0 0 4.5 0zm0 6.3a1.8 1.8 0 1 1 0-3.6 1.8 1.8 0 0 1 0 3.6z" fill="#fff"/></svg>123, Pebbleton coaching and organization Company.</span>
  <span style="left:771px"><svg width="11" height="11" viewBox="0 0 24 24"><path d="M6.6 10.8a15 15 0 0 0 6.6 6.6l2.2-2.2c.3-.3.7-.4 1-.2 1.1.4 2.3.6 3.6.6.6 0 1 .4 1 1V20c0 .6-.4 1-1 1A17 17 0 0 1 3 4c0-.6.4-1 1-1h3.5c.6 0 1 .4 1 1 0 1.3.2 2.5.6 3.6.1.3 0 .7-.2 1z" fill="#fff"/></svg>+ 1 555 010 2040</span>
  <span style="left:943px"><svg width="13" height="10" viewBox="0 0 13 10"><rect width="13" height="10" rx="1" fill="#fff"/><path d="M0 1l6.5 4.5L13 1" stroke="#0f5fa8" fill="none"/></svg>hello@pebbleton.example</span>
</div>

<nav class="abs nav">
  <a style="left:113px">Home</a>
  <a style="left:190px">About Us</a>
  <a style="left:288px">Categories</a>
  <a style="left:398px">News</a>
  <a style="left:751px">Contact Us</a>
  <svg class="abs" style="left:857px;top:21px" width="20" height="20" viewBox="0 0 20 20"><circle cx="8" cy="8" r="6" stroke="#0f5fa8" stroke-width="3" fill="none"/><path d="M12.5 12.5L18 18" stroke="#0f5fa8" stroke-width="3.2" stroke-linecap="round"/></svg>
  <div class="abs btn" style="left:916px;top:13px;width:172px;height:38px">Get Started</div>
</nav>

<section class="abs hero">
  <div class="abs" role="img" aria-label="Smiling family relaxing together on a sofa" style="inset:0;background:linear-gradient(100deg,#4a4640 0%,#6d6258 35%,#5d5a52 60%,#3f4a3c 100%)"></div>
  <svg class="abs" style="left:0;top:560px" width="1200" height="90" viewBox="0 0 1200 90">
    <path d="M0 85 C250 -10 450 40 700 65 C900 85 1080 70 1200 40 L1200 90 L0 90 Z" fill="#f8cf3a"/>
    <path d="M0 88 C250 10 450 50 700 75 C900 95 1080 82 1200 60 L1200 90 L0 90 Z" fill="#fff"/>
  </svg>
  <h1>Welcome To Pebbleton</h1>
  <div class="abs btn" style="left:112px;top:382px;width:170px;height:38px">Contact Us</div>
  <div class="abs phone" style="left:740px;top:135px;width:150px;height:345px"><div role="img" aria-label="Child lying on grass" style="background:linear-gradient(160deg,#5f8a3a,#9bbd6a)"></div></div>
  <div class="abs phone" style="left:1005px;top:135px;width:155px;height:345px"><div role="img" aria-label="Friends laughing together" style="background:linear-gradient(160deg,#7a6a62,#c9a58c)"></div></div>
  <div class="abs phone" style="left:862px;top:124px;width:172px;height:360px"><div role="img" aria-label="Parent carrying child on shoulders at the beach" style="background:linear-gradient(180deg,#8cc7e0,#cfd9d6 60%,#b9a28a)"></div></div>
</section>

<svg class="abs logo-plate" viewBox="0 0 169 176"><path d="M0 0H169V134L84.5 176L0 134Z" fill="#fff"/></svg>
<svg class="abs" style="left:586px;top:18px" width="30" height="30"><circle cx="15" cy="15" r="14" fill="#1a56a0"/></svg>
<div class="abs brand">Pebbleton</div>

<h2 class="abs cat-title">Categories</h2>
<svg class="abs arrow" style="left:59px" viewBox="0 0 35 35"><circle cx="17.5" cy="17.5" r="17.5" fill="#e3204f"/><path d="M25 17.5H11M17 10.5l-7 7 7 7" stroke="#fff" stroke-width="4" fill="none" stroke-linecap="round" stroke-linejoin="round"/></svg>
<div class="abs cat" role="img" aria-label="Children running outdoors" style="left:113px;background:linear-gradient(180deg,#6f8f5a 0%,#5b9a3c 50%,#0fa81c 100%)">Children</div>
<div class="abs cat" role="img" aria-label="Smiling family group" style="left:453px;background:linear-gradient(180deg,#c9c0b0 0%,#d9b95a 50%,#f5c80a 100%)">Family</div>
<div class="abs cat" role="img" aria-label="Group of happy friends" style="left:792px;background:linear-gradient(180deg,#8f98a8 0%,#4d7aa8 50%,#0a5ea8 100%)">Friends</div>
<svg class="abs arrow" style="left:1105px" viewBox="0 0 35 35"><circle cx="17.5" cy="17.5" r="17.5" fill="#e3204f"/><path d="M10 17.5H24M18 10.5l7 7-7 7" stroke="#fff" stroke-width="4" fill="none" stroke-linecap="round" stroke-linejoin="round"/></svg>

<article class="feature">
  <div class="abs feature-img" role="img" aria-label="Circle of laughing children looking down at the camera"></div>
  <h2>Lorem Ipsum Dolor Sit</h2>
  <p style="top:1792px">Sed ut perspiciatis unde omnis iste natus error sit voluptatem accusantium doloremque laudantium, totam rem aperiam, eaque ipsa quae ab illo inventore veritatis et quasi architecto beatae vitae dicta sunt explicabo.</p>
  <p style="top:1895px">Nemo enim ipsam voluptatem quia voluptas sit aspernatur aut odit aut fugit, sed quia consequuntur magni dolores eos qui ratione voluptatem sequi nesciunt. Neque porro quisquam est, qui dolorem ipsum quia dolor sit amet, consectetur, adipisci velit, sed quia non numquam eius modi tempora incidunt ut labore et dolore magnam aliquam quaerat voluptatem.</p>
  <p style="top:2049px">Lorem ipsum dolor sit amet, consectetur adipiscing elit, sed do eiusmod tempor incididunt ut labore et dolore magna aliqua. Ut enim ad minim veniam, quis nostrud exercitation ullamco laboris nisi ut aliquip ex ea commodo consequat.</p>
  <div class="abs readmore">[Click Here To Read More]</div>
</article>

<aside>
  <div class="abs news"></div>
  <div class="abs news-head">Our News</div>
  <div class="abs item" style="top:1368px">
    <div class="thumb" role="img" aria-label="Group of children smiling" style="background:linear-gradient(120deg,#7aa84a,#e0b070,#d94a3a)"></div>
    <h3>Lorem Ipsum Dolor Sit</h3><time>Feb 05,2024</time>
    <p>Excepteur sint occaecat cupidatat non proident, sunt in culpa qui officia deserunt mollit anim id est laborum.</p>
    <a>Read More</a>
  </div>
  <div class="abs item" style="top:1642px">
    <div class="thumb" role="img" aria-label="Two friends hugging in the city" style="background:linear-gradient(120deg,#8aa0b8,#d8b090,#6a7f98)"></div>
    <h3>Finibus Bonorum et</h3><time>Feb 05,2024</time>
    <p>Excepteur sint occaecat cupidatat non proident, sunt in culpa qui officia deserunt mollit anim id est laborum.</p>
    <a>Read More</a>
  </div>
  <div class="abs item" style="top:1915px">
    <div class="thumb" role="img" aria-label="Family embracing at home" style="background:linear-gradient(120deg,#d8d4cc,#8a8060,#c9b8a4)"></div>
    <h3>Nemo enim ipsam</h3><time>Feb 05,2024</time>
    <p>Excepteur sint occaecat cupidatat non proident, sunt in culpa qui officia deserunt mollit anim id est laborum.</p>
    <a>Read More</a>
  </div>
</aside>

<footer class="abs footer">
  <div class="links">Terms Of Use<span class="sep">|</span>Privacy Policy<span class="sep">|</span>Copyright © 2024 Pebbleton. All rights reserved.</div>
  <svg class="abs" style="left:770px;top:50px" width="120" height="26" aria-label="Social links">
    <circle cx="13" cy="13" r="11" fill="none" stroke="#fff" stroke-width="2"/>
    <circle cx="55" cy="13" r="11" fill="none" stroke="#fff" stroke-width="2"/>
    <circle cx="97" cy="13" r="11" fill="none" stroke="#fff" stroke-width="2"/>
  </svg>
  <svg class="abs" style="left:1029px;top:22px" width="28" height="28"><circle cx="14" cy="14" r="13" fill="#fff"/></svg>
  <div class="abs" style="left:985px;top:60px;width:116px;text-align:center;font-weight:700;font-size:19px">Pebbleton</div>
</footer>

</body>
</html>
```